Customs House descriptive business cards

We require a two-sided business card that has a simple yet elegant design. We want to be able to promote our services as a customs house. This card should include our logo, contact info and services offered with the logo being on one side and the contact info and services on the flip side

Target Market(s)

Importers / exporters to and from the Bahamas

Industry/Entity Type

Logistics

Contact Information for Business Card

The front side of the card could have the logo and the flip side should have the other relevant info

Font styles to use
Serif

Colors

Designer to choose colors to be used in the design.

Requirements
Must have
• (Harbourline Agents Ltd) Logo, address and contact info also services:
• import customs clearance, Delivery & HAndling services,Florida pickups, Export packing & Crating Services, export customs clearance, Consulting

```html
<!DOCTYPE html>
<html lang="en">
<head>
<meta charset="utf-8">
<title>Harbourline Agents Ltd – Business Card</title>
<link href="https://fonts.googleapis.com/css2?family=Cinzel:wght@600&family=Lato:wght@400&display=swap" rel="stylesheet">
<style>
  :root {
    --page-bg: #e9e6e1;
    --brand-blue: #3f66b0;
    --brand-blue-light: #5b9bd8;
    --brand-blue-deep: #3a5ca6;
    --accent-blue: #4a8fd4;
    --ink: #2b2b2b;
    --rule: #a9a9a9;
    --white: #ffffff;
  }
  * { margin: 0; padding: 0; box-sizing: border-box; }
  html, body {
    width: 1200px; height: 1194px; overflow: hidden;
    background: var(--page-bg);
  }
  .card {
    position: absolute;
    left: 160px;
    width: 880px;
    height: 500px;
    border-radius: 34px;
    overflow: hidden;
    box-shadow: 0 14px 24px rgba(0,0,0,0.18);
  }
  /* Front side */
  .card--front {
    top: 40px;
    background: radial-gradient(ellipse 60% 70% at 50% 50%, var(--brand-blue-light) 0%, var(--brand-blue) 70%, var(--brand-blue-deep) 100%);
    color: var(--white);
  }
  .front-brand {
    position: absolute;
    top: 205px; left: 0; right: 0;
    display: flex; align-items: center; justify-content: center; gap: 18px;
  }
  .brand-dot {
    width: 26px; height: 26px; border-radius: 50%;
    background: var(--white);
  }
  .front-brand .brand-name {
    font-family: "Cinzel", Georgia, serif;
    font-weight: 600;
    font-size: 46px;
    color: var(--white);
    letter-spacing: 1px;
  }
  .service-list {
    position: absolute;
    left: 66px; right: 62px; top: 408px;
    list-style: none;
    font-family: "Lato", Arial, sans-serif;
    font-size: 18.5px;
    line-height: 27px;
    display: grid;
    grid-template-columns: auto auto auto;
    justify-content: space-between;
    row-gap: 0;
  }
  .service-list li::before {
    content: "";
    display: inline-block;
    width: 7px; height: 7px; border-radius: 50%;
    background: var(--white);
    margin: 0 14px 3px 0;
    vertical-align: middle;
  }
  /* Back side */
  .card--back {
    top: 620px;
    background: var(--white);
    color: var(--ink);
    font-family: "Lato", Arial, sans-serif;
  }
  .back-brand {
    position: absolute;
    left: 63px; top: 250px;
    font-family: "Cinzel", Georgia, serif;
    font-weight: 600;
    font-size: 29px;
    color: var(--brand-blue);
  }
  .holder {
    position: absolute;
    right: 62px; top: 262px;
    text-align: right;
  }
  .holder-name {
    font-size: 40px;
    line-height: 46px;
    color: var(--accent-blue);
  }
  .holder-title {
    font-size: 20px;
    line-height: 26px;
  }
  .divider {
    position: absolute;
    left: 63px; right: 62px; top: 351px;
    height: 1px; background: var(--rule);
  }
  .contact-list {
    position: absolute;
    left: 63px; top: 365px;
    list-style: none;
    font-size: 20.5px;
    line-height: 27px;
    letter-spacing: 0.6px;
  }
  .contact-list li { display: flex; align-items: center; gap: 14px; }
  .contact-list svg { width: 17px; height: 17px; fill: var(--brand-blue); flex: none; }
  .address {
    position: absolute;
    right: 62px; top: 365px;
    text-align: right;
    font-style: normal;
    font-size: 20.5px;
    line-height: 27px;
    letter-spacing: 0.6px;
  }
</style>
</head>
<body>
  <section class="card card--front" aria-label="Card front">
    <div class="front-brand">
      <span class="brand-dot"></span>
      <span class="brand-name">Harbourline Agents Ltd</span>
    </div>
    <ul class="service-list">
      <li>Import customs clearance</li>
      <li>Delivery &amp; Handling services</li>
      <li>Florida pickups</li>
      <li>Export packing &amp; Crating Services</li>
      <li>Export customs clearance</li>
      <li>Consulting</li>
    </ul>
  </section>

  <section class="card card--back" aria-label="Card back">
    <div class="back-brand">Harbourline Agents Ltd</div>
    <div class="holder">
      <div class="holder-name">Dana Whitfield</div>
      <div class="holder-title">Founder &amp; CEO</div>
    </div>
    <div class="divider"></div>
    <ul class="contact-list">
      <li>
        <svg viewBox="0 0 24 24" aria-hidden="true"><path d="M6.6 10.8a15.1 15.1 0 0 0 6.6 6.6l2.2-2.2a1 1 0 0 1 1-.25 11.4 11.4 0 0 0 3.6.57 1 1 0 0 1 1 1V20a1 1 0 0 1-1 1A17 17 0 0 1 3 4a1 1 0 0 1 1-1h3.5a1 1 0 0 1 1 1c0 1.25.2 2.45.57 3.6a1 1 0 0 1-.25 1z"/></svg>
        +1 242 555 0148
      </li>
      <li>
        <svg viewBox="0 0 24 24" aria-hidden="true"><path d="M2 5h20v14H2z M2 6l10 7 10-7" /></svg>
        info@harbourlineagents.com
      </li>
      <li>
        <svg viewBox="0 0 24 24" aria-hidden="true"><path d="M12 2a10 10 0 1 0 0 20 10 10 0 0 0 0-20zm6.9 6h-3a15.6 15.6 0 0 0-1.4-3.6A8 8 0 0 1 18.9 8zM12 4c.8 1.2 1.5 2.5 1.9 4h-3.8c.4-1.5 1.1-2.8 1.9-4zM4.3 14a8 8 0 0 1 0-4h3.4a16.5 16.5 0 0 0 0 4zm.8 2h3a15.6 15.6 0 0 0 1.4 3.6A8 8 0 0 1 5.1 16zm3-8h-3a8 8 0 0 1 4.3-3.6A15.6 15.6 0 0 0 8.1 8zM12 20c-.8-1.2-1.5-2.5-1.9-4h3.8c-.4 1.5-1.1 2.8-1.9 4zm2.3-6H9.7a14.7 14.7 0 0 1 0-4h4.6a14.7 14.7 0 0 1 0 4zm.3 5.6a15.6 15.6 0 0 0 1.4-3.6h3a8 8 0 0 1-4.4 3.6zM16.3 14a16.5 16.5 0 0 0 0-4h3.4a8 8 0 0 1 0 4z"/></svg>
        www.harbourlineagents.com
      </li>
    </ul>
    <address class="address">
      Meridian Tower<br>
      2nd floor, Office 204/206<br>
      P.O.Box: 420816
    </address>
  </section>
</body>
</html>
```